Winery Needs a flyer for a dinner show with a tribute band/show

We will have a dinner and show with hosted beer and wine. The show will be a tribute to the Moon Crew. The event will be on November 1, 2019 from 6pm-10pm with dinner starting at 6:30pm. Would like to have on the flyer GTL DinnerGuild Presents... A tribute to the Moon Crew. Enjoy an evening with the Stars under the Stars on the HillPaths.... Club Members $159.00 General Public $189.00 tickets can be purchased online at www.HillPathCellars.example, call in 555.304.7712 or at the Sipping Hall, 4870 Marbrook Court Fairfield, Ca 90001. Included files as example and some of our logos. Just examples looking forward to your creativity.

Target Market(s)

Wine Drinkers, age 30-60, outdoor people

Font styles to use
Sans Serif
Other font styles liked:
• cottage and Barn

Colors

Designer to choose colors to be used in the design.

Requirements
Must have
• All important information to purchase tickets
Nice to have
• classic and reto if possible while still incorporating our logo somewhere

```html
<!DOCTYPE html>
<html lang="en">
<head>
<meta charset="utf-8">
<title>A Tribute to the Moon Crew – GTL DinnerGuild</title>
<link rel="stylesheet" href="https://fonts.googleapis.com/css2?family=Kaushan+Script&family=IM+Fell+Double+Pica&family=Roboto:wght@500;700;900&display=swap">
<style>
  :root {
    --bg: #8a8d8f;
    --paper: #ffffff;
    --amber: #f0a02a;
    --amber-deep: #d98a1e;
    --amber-glow: #f2a93a;
    --brown: #3a1f0a;
    --brown-mid: #6b3c12;
    --ink: #0d0a08;
    --fade-grey: #b9b9b9;
    --text-white: #ffffff;
    --logo-green: #5a7a3a;
  }
  html, body {
    margin: 0;
    padding: 0;
    width: 1200px;
    height: 1200px;
    overflow: hidden;
    background: var(--bg);
  }
  .flyer {
    position: absolute;
    left: 160px;
    top: 26px;
    width: 880px;
    height: 1148px;
    background: var(--paper);
    overflow: hidden;
    box-shadow: 0 6px 24px rgba(0,0,0,.35);
    font-family: "Roboto", Arial, sans-serif;
  }
  .flyer p, .flyer h1, .flyer h2 { margin: 0; }

  /* photo area: soft tonal stand-in for the halftone group portrait */
  .hero-photo {
    position: absolute;
    left: 0; top: 0;
    width: 880px; height: 800px;
    background:
      radial-gradient(ellipse 150px 210px at 110px 330px, rgba(240,160,42,.55), transparent 70%),
      radial-gradient(ellipse 130px 200px at 330px 360px, rgba(240,160,42,.6), transparent 70%),
      radial-gradient(ellipse 120px 190px at 560px 340px, rgba(240,160,42,.6), transparent 70%),
      radial-gradient(ellipse 140px 210px at 750px 330px, rgba(240,160,42,.5), transparent 70%),
      radial-gradient(ellipse 520px 160px at 440px 80px, var(--amber-glow), transparent 75%),
      linear-gradient(180deg,
        var(--amber-deep) 0%,
        var(--brown-mid) 30%,
        var(--brown) 52%,
        var(--ink) 72%,
        #1c1c1c 82%,
        var(--fade-grey) 94%,
        #dedede 100%);
  }

  .presenter {
    position: absolute;
    left: 40px; top: 552px;
    width: 200px;
    text-align: right;
    color: var(--amber);
    font-weight: 700;
    font-size: 21px;
    line-height: 1.05;
  }
  .tribute-line {
    position: absolute;
    left: 252px; top: 532px;
    color: var(--text-white);
    font-family: "Kaushan Script", cursive;
    font-weight: 400;
    font-size: 70px;
    line-height: 1;
  }
  .show-title {
    position: absolute;
    left: 0; top: 612px;
    width: 880px;
    padding-left: 30px;
    box-sizing: border-box;
    text-align: center;
    color: var(--amber);
    font-family: "Kaushan Script", cursive;
    font-weight: 400;
    font-size: 122px;
    line-height: 1.2;
    white-space: nowrap;
    text-shadow: 0 3px 6px rgba(0,0,0,.45);
  }

  .tagline-band {
    position: absolute;
    left: 0; top: 792px;
    width: 880px; height: 104px;
    background: linear-gradient(90deg, var(--amber-deep), var(--amber));
  }
  .tagline {
    position: absolute;
    left: 0; top: 806px;
    width: 880px;
    text-align: center;
    font-family: "IM Fell Double Pica", Georgia, serif;
    font-size: 37px;
    line-height: 1;
    color: var(--ink);
    letter-spacing: 1px;
    text-transform: uppercase;
  }

  .event-when {
    position: absolute;
    left: 0; top: 912px;
    width: 880px;
    text-align: center;
    font-weight: 900;
    font-size: 33px;
    line-height: 1.08;
    color: var(--ink);
  }

  .brand {
    position: absolute;
    left: 56px; top: 1022px;
    width: 190px;
    display: flex;
    align-items: center;
    gap: 10px;
    color: var(--logo-green);
    font-weight: 700;
    font-size: 27px;
    line-height: 1.05;
  }
  .brand-dot {
    flex: none;
    width: 22px; height: 22px;
    border-radius: 50%;
    background: var(--logo-green);
  }

  .ticket-info {
    position: absolute;
    left: 250px; top: 1004px;
    width: 620px;
    font-weight: 700;
    font-size: 20px;
    line-height: 1.3;
    color: var(--amber-deep);
  }
  .ticket-info .dark { color: var(--ink); }
</style>
</head>
<body>
  <main class="flyer">
    <div class="hero-photo" role="img" aria-label="Amber-toned halftone photo of four singers in tuxedos holding microphones"></div>

    <p class="presenter">GTL DinnerGuild<br>presents...</p>
    <h2 class="tribute-line">A Tribute to</h2>
    <h1 class="show-title">The Moon Crew</h1>

    <div class="tagline-band"></div>
    <p class="tagline">Enjoy an evening with the stars<br>under the stars on the HillPaths . . .</p>

    <p class="event-when">NOVEMBER 1, 2019 FROM 6PM-10PM<br>WITH DINNER STARTING AT 6:30PM.</p>

    <div class="brand">
      <span class="brand-dot"></span>
      <span>Hill Path Cellars</span>
    </div>

    <p class="ticket-info">
      <span class="dark">Club Members</span> $159.00 General Public <span class="dark">$189.00</span><br>
      Tickets can be purchased online at<br>
      www.HillPathCellars.example, call in 555.304.7712 or<br>
      at the Sipping Hall, 4870 Marbrook Court Fairfield, Ca 90001.
    </p>
  </main>
</body>
</html>
```